Pitch book for Birchvale Real Estate Investors.

Birchvale Investors is a new real estate investment company focused on multifamily (apartment) investments along the San Francisco Peninsula (in other parts of the world it is also referred to as flats). We need a professional Pitch Book i.e. brochure (digital and print) to raise equity from private investors. Read about “pitch book” on Wikipedia. The profile of the investor is conservative and must qualify as an accredited investor. Think high net worth individuals, CEOs and wealthy retiring couples. The investor that is attracted to real estate invest because it is low risk, produce cash flow and provide solid returns over the long term.

The brochure should convey trust, be highly professional and be clean and crisp. I attach a PowerPoint doc to be used as a copy for the brochure. I also attach a brochure of Harlow Pike – I like the look and feel, think it was designed with InDesign.

We will use the brochure at one-on-one meetings with investors where we will present on a laptop; we also need it in a format so that we can email it, print it and use it to be uploaded as a website.

I prefer the up and down scroll format (like you would do on a Mac) compared to PowerPoint but I am open to suggestions.

The photos I used in the PowerPoint presentation was found on the web, please use your own stock images.

Target Market(s)

High net worth individuals

Industry/Entity Type

Real Estate

Font styles to use
Serif

Requirements
Must have
• See attached Power Point
Nice to have
• See attached HPK brochure, I like the look and feel.
Should not have
• I am open to your ideas.

```html
<!DOCTYPE html>
<html lang="en">
<head>
<meta charset="utf-8">
<title>Birchvale — San Francisco Peninsula Multifamily Real Estate Investment</title>
<link href="https://fonts.googleapis.com/css2?family=Open+Sans:wght@300;400;600;700&display=swap" rel="stylesheet">
<style>
  :root {
    --backdrop: #e6e6e4;
    --paper: #ffffff;
    --ink: #3d3d3d;
    --ink-soft: #6a6a6a;
    --ink-faint: #9a9a9a;
    --accent: #3d79c4;
    --rule: #bdbdbd;
    --sky-top: #1d4fa8;
    --sky-mid: #6a7fb8;
    --dusk: #d9a3a0;
    --water: #3c4a78;
    --bridge: #d8541e;
    --archive-light: #cfcfcf;
    --archive-dark: #4a4a4a;
    --city-dark: #1b2038;
    --city-glow: #c98a45;
  }
  * { box-sizing: border-box; margin: 0; padding: 0; }
  html, body { width: 897px; height: 1200px; overflow: hidden; }
  body {
    background: var(--backdrop);
    font-family: "Open Sans", Arial, sans-serif;
    color: var(--ink);
    position: relative;
  }
  .page {
    position: absolute;
    background: var(--paper);
    box-shadow: 0 2px 6px rgba(0,0,0,.18);
    overflow: hidden;
  }

  /* Cover */
  .cover { left: 30px; top: 30px; width: 837px; height: 538px; }
  .cover-photo {
    position: absolute; left: 0; top: 0; width: 837px; height: 445px;
    background:
      radial-gradient(ellipse 30% 60% at 56% 55%, rgba(216,84,30,.85), rgba(216,84,30,0) 70%),
      linear-gradient(180deg, var(--sky-top) 0%, var(--sky-mid) 38%, var(--dusk) 52%, var(--water) 62%, #2a3560 100%);
  }
  .cover-brand {
    position: absolute; right: 30px; top: 52px;
    display: flex; align-items: center; gap: 7px;
    color: #fff; font-size: 14px; font-weight: 400; letter-spacing: .5px;
  }
  .cover-brand .mark { width: 10px; height: 10px; background: #fff; }
  .cover-footer {
    position: absolute; left: 0; top: 445px; width: 837px; height: 93px;
    display: flex;
  }
  .cover-footer .legal-band {
    width: 420px; height: 100%;
    background: linear-gradient(90deg, #fff 0%, #f3f3f3 70%, #e4e4e4 100%);
    position: relative;
  }
  .footer-brand {
    position: absolute; left: 19px; top: 64px;
    font-size: 13px; color: var(--ink-faint); letter-spacing: .4px;
    display: flex; align-items: center; gap: 6px;
  }
  .footer-brand .mark { width: 9px; height: 9px; background: var(--archive-light); }
  .legal {
    position: absolute; left: 115px; top: 16px; width: 290px;
    font-size: 9.4px; line-height: 1.18; color: var(--ink-soft);
  }
  .cover-title { flex: 1; text-align: right; padding: 23px 54px 0 0; }
  .cover-title h1 {
    font-weight: 300; font-size: 31px; color: var(--ink); letter-spacing: -.2px; line-height: 1.1;
  }
  .cover-title p {
    font-size: 13.5px; color: var(--accent); letter-spacing: 1.5px; margin-top: 4px; text-transform: uppercase;
  }

  /* Inside spread */
  .spread { left: 27px; top: 598px; width: 840px; height: 546px; }
  .archive-photo {
    position: absolute; left: 0; top: 0; width: 163px; height: 546px;
    background: linear-gradient(160deg, var(--archive-light) 0%, #9a9a9a 35%, #6c6c6c 70%, var(--archive-dark) 100%);
  }
  .folio { position: absolute; bottom: 12px; font-size: 8px; color: var(--ink); }
  .folio.left { left: 18px; color: #fff; }
  .folio.right { right: 18px; }

  .opportunity {
    position: absolute; left: 163px; top: 0; width: 259px; height: 546px;
    background: linear-gradient(90deg, #fff 0%, #f7f7f7 60%, #e8e8e8 100%);
  }
  .section-head { text-align: center; }
  .section-head h2 {
    font-weight: 400; font-size: 17px; color: var(--accent); letter-spacing: 2px; text-transform: uppercase;
  }
  .section-head .tagline {
    font-weight: 300; font-size: 11.5px; color: var(--ink-soft); letter-spacing: 1px; line-height: 1.2; margin-top: 8px;
  }
  .opportunity .section-head { padding-top: 17px; }
  .opportunity .rule { width: 120px; height: 1px; background: var(--rule); margin: 18px auto 0; }
  .lead {
    position: absolute; left: 30px; top: 151px; width: 225px;
    font-weight: 600; font-size: 11.3px; line-height: 1.2; color: var(--ink);
  }
  .reasons { position: absolute; left: 30px; top: 294px; width: 215px; }
  .reasons h3 { font-weight: 400; font-size: 11.3px; color: var(--ink); margin-bottom: 16px; }
  .reasons li {
    list-style: none; font-weight: 300; font-size: 11.3px; line-height: 1.35; color: var(--ink-soft); margin-bottom: 15px;
  }

  .mission { position: absolute; left: 422px; top: 0; width: 418px; height: 546px; }
  .mission .section-head { padding-top: 17px; width: 375px; }
  .mission .tagline { margin-top: 6px; }
  .mission-body {
    position: absolute; left: 24px; top: 104px; width: 376px;
    font-weight: 300; font-size: 11.5px; line-height: 1.1; color: var(--ink);
  }
  .mission h3 { font-weight: 600; font-size: 11.5px; color: var(--ink); }
  .focus-q { position: absolute; left: 24px; top: 174px; }
  .focus-a {
    position: absolute; left: 24px; top: 197px; width: 376px;
    font-weight: 600; font-size: 8.2px; line-height: 1.2; color: var(--ink); text-align: justify;
  }
  .city-photo {
    position: absolute; left: 23px; top: 248px; width: 395px; height: 122px;
    background:
      radial-gradient(ellipse 40% 60% at 50% 80%, var(--city-glow), rgba(201,138,69,0) 70%),
      linear-gradient(180deg, #3a4870 0%, #2a3150 35%, var(--city-dark) 60%, #3a2a22 100%);
  }
  .why-q { position: absolute; left: 24px; top: 396px; }
  .why-list { position: absolute; left: 24px; top: 420px; width: 385px; }
  .why-list li {
    list-style: none; font-weight: 300; font-size: 11.3px; line-height: 1.12; color: var(--ink);
  }
</style>
</head>
<body>

<section class="page cover">
  <div class="cover-photo" role="img" aria-label="Photograph of a red suspension bridge tower at dusk with the bay and city skyline behind"></div>
  <div class="cover-brand"><span class="mark"></span>BIRCHVALE</div>
  <div class="cover-footer">
    <div class="legal-band">
      <div class="footer-brand"><span class="mark"></span>BIRCHVALE</div>
      <p class="legal">This document does not represent an offer to sell or solicitation of an offer to purchase any real estate or securities. Any such offering will be made only pursuant to definitive offering documents in a private placement limited to accredited investors.</p>
    </div>
    <div class="cover-title">
      <h1>San Francisco Peninsula</h1>
      <p>Multifamily Real Estate Investment</p>
    </div>
  </div>
</section>

<section class="page spread">
  <div class="archive-photo" role="img" aria-label="Black and white archival photograph of a historic corner apartment building with a cable car in the street"></div>
  <span class="folio left">1</span>

  <div class="opportunity">
    <header class="section-head">
      <h2>Your Opportunity</h2>
      <p class="tagline">....safety, cash flow and<br>appreciation</p>
    </header>
    <div class="rule"></div>
    <p class="lead">Birchvale Investors is pleased to offer you the opportunity to invest in the San Francisco Peninsula multifamily real estate market.</p>
    <div class="reasons">
      <h3>Why invest and why here?</h3>
      <ul>
        <li>• Investing in real estate is recognized as a significant wealth-creation strategy.</li>
        <li>• The San Francisco Peninsula is one of the top real estate markets in the world.</li>
        <li>• The multifamily asset class is considered a low risk investment.</li>
      </ul>
    </div>
  </div>

  <div class="mission">
    <header class="section-head">
      <h2>Our Mission</h2>
      <p class="tagline">....to protect and grow your investment<br>FIND, BUY, HOLD FOR THE LONG-TERM</p>
    </header>
    <p class="mission-body">Birchvale Investors’ core goal is to identify investments that produce consistent cash flow, have long-term value prospects not currently recognized by the market, and once acquired, increase their operational and managerial efficiencies to maximize cash flow and capital appreciation.</p>
    <h3 class="focus-q">Why focus on a specific asset class and geography?</h3>
    <p class="focus-a">A focused approach is one of our competitive advantages. With 20 years real estate investment and development experience, Birchvale Investors is a Silicon Valley-based multifamily investment and advisory firm, laser-focused on growing cash flow and lasting value for our clients.</p>
    <div class="city-photo" role="img" aria-label="Night aerial photograph of the San Francisco skyline and bay bridge lights"></div>
    <h3 class="why-q">Why invest and why here?</h3>
    <ul class="why-list">
      <li>• In existing properties - we can evaluate existing expenses and rent rolls with more certainty;</li>
      <li>• In select San Francisco and Silicon Valley locations - we know the streets and neighborhoods;</li>
      <li>• Using low risk core and core plus investment strategies - to reasonably predict cash flow; and</li>
      <li>• For the long-term - your investment is a safe-haven that endures market fluctuations.</li>
    </ul>
  </div>
  <span class="folio right">2</span>
</section>

</body>
</html>
```